LumaStudy full page advertisement

I have attached a pdf document with design requirements and specifics as well as a logo. The only addition is to add "LumaStudy" under the logo as it is displayed on the website lumastudy.com

Target Market(s)

Online Education for chiropractors

Industry/Entity Type

Online Education

Requirements
Must have
• Please see attached document
Nice to have
Should not have

```html
<!DOCTYPE html>
<html lang="en">
<head>
<meta charset="utf-8">
<title>LumaStudy — Full Page Advertisement</title>
<link rel="stylesheet" href="https://fonts.googleapis.com/css2?family=Playfair+Display:wght@700&family=Open+Sans:wght@400;700&display=swap">
<style>
  :root {
    --navy: #0d1b4c;
    --lavender: #cdd0e3;
    --lavender-light: #e9eaf2;
    --slate: #80838c;
    --slate-dark: #6e7179;
    --rule: #8d8f96;
    --ink: #2b2d33;
    --white: #ffffff;
  }
  * { margin: 0; padding: 0; box-sizing: border-box; }
  html, body { width: 912px; height: 1200px; overflow: hidden; background: var(--white); }
  .stage { position: relative; width: 912px; height: 1200px; }
  .page {
    position: absolute; left: 115px; top: 118px; width: 682px; height: 963px;
    box-shadow: 6px 8px 14px rgba(0,0,0,0.28);
    overflow: hidden;
  }
  .page-art { position: absolute; inset: 0; width: 682px; height: 963px; }
  .content { position: absolute; inset: 0; }
  .brand {
    position: absolute; left: 60px; top: 44px; width: 220px; text-align: center;
    font-family: "Playfair Display", serif; font-weight: 700; font-size: 30px;
    color: var(--navy);
  }
  .site-url {
    position: absolute; left: 40px; top: 116px; width: 262px; text-align: center;
    font-family: "Open Sans", sans-serif; font-size: 10.5px; letter-spacing: 4.6px;
    color: var(--ink);
  }
  .feature {
    position: absolute; left: 21px; width: 300px; text-align: center;
    font-family: "Playfair Display", serif; font-weight: 700; font-size: 19.5px;
    line-height: 24.5px; color: var(--navy);
  }
  .feature--history { top: 159px; }
  .feature--library { top: 285px; }
  .feature--webinars { top: 411px; }
  .divider { position: absolute; left: 47px; width: 249px; height: 12px; }
  .divider::before, .divider::after {
    content: ""; position: absolute; top: 5px; width: 112px; height: 1px; background: var(--rule);
  }
  .divider::before { left: 0; }
  .divider::after { right: 0; }
  .divider span {
    position: absolute; left: 119px; top: 0; width: 11px; height: 11px; border-radius: 50%;
    background: var(--rule);
  }
  .divider--one { top: 267px; }
  .divider--two { top: 393px; }
  .divider--three { top: 517px; }
  .programs {
    position: absolute; left: 21px; top: 541px; width: 300px; text-align: center;
    font-family: "Open Sans", sans-serif; color: var(--ink);
  }
  .programs h2 {
    font-size: 16.5px; line-height: 23px; font-weight: 700; color: var(--navy); margin-bottom: 8px;
  }
  .programs ul { list-style: none; font-size: 14px; line-height: 17.5px; }
  .programs li { position: relative; padding-left: 14px; margin-bottom: 8px; }
  .programs li::before {
    content: ""; position: absolute; left: 16px; top: 6px;
    border-left: 5px solid var(--ink); border-top: 3px solid transparent; border-bottom: 3px solid transparent;
  }
  .assistant-cta {
    position: absolute; left: 60px; top: 727px; width: 345px; height: 99px;
    background: var(--navy); color: var(--white); text-align: center;
    box-shadow: 0 6px 10px rgba(0,0,0,0.25);
  }
  .assistant-cta h3 {
    font-family: "Playfair Display", serif; font-weight: 700; font-size: 16.5px;
    margin-top: 19px;
  }
  .assistant-cta p {
    font-family: "Open Sans", sans-serif; font-size: 11.4px; line-height: 16px; margin-top: 8px;
  }
</style>
</head>
<body>
<div class="stage">
  <div class="page">
    <svg class="page-art" viewBox="0 0 682 963" xmlns="http://www.w3.org/2000/svg">
      <defs>
        <linearGradient id="panelGrad" x1="0" y1="0" x2="0" y2="1">
          <stop offset="0" stop-color="#cdd0e3"/>
          <stop offset="0.5" stop-color="#e9eaf2"/>
          <stop offset="1" stop-color="#c9cce0"/>
        </linearGradient>
        <radialGradient id="spineGrad" cx="0.6" cy="0.5" r="0.6">
          <stop offset="0" stop-color="#c9cbd0"/>
          <stop offset="0.35" stop-color="#9a9ca3"/>
          <stop offset="1" stop-color="#7f828b"/>
        </radialGradient>
      </defs>
      <rect width="682" height="963" fill="url(#panelGrad)"/>
      <path role="img" aria-label="Illustration of the human spine and rib cage in grey tones"
            d="M160 0 L682 0 L682 963 L89 963 C190 870 290 720 360 560 C430 400 462 220 460 56 C390 28 280 8 160 0 Z"
            fill="url(#spineGrad)"/>
      <path d="M160 0 C290 8 410 28 468 50 L468 56 C460 56 460 56 460 56 C390 30 280 9 160 0 Z" fill="#0d1b4c"/>
      <path d="M150 0 C300 10 420 32 466 52 C470 220 434 400 362 562 C292 722 192 872 89 963"
            fill="none" stroke="#0d1b4c" stroke-width="5"/>
      <path d="M60 826 L240 826 L170 870 Z" fill="#8a8c93"/>
    </svg>
    <div class="content">
      <div class="brand">LumaStudy</div>
      <div class="site-url">www.LumaStudy.com</div>

      <p class="feature feature--history">serving the Continuing<br>Education Needs of<br>the Chiropractic Profession<br>Worldwide since 2001</p>
      <div class="divider divider--one"><span></span></div>

      <p class="feature feature--library">Over 2000 hours of On Demand<br>courses in more than 75 topics<br>by leading minds in the<br>Chiropractic Profession</p>
      <div class="divider divider--two"><span></span></div>

      <p class="feature feature--webinars">Real Time Webinars every<br>week in a huge variety of<br>topics of interest to the<br>Chiropractic Profession</p>
      <div class="divider divider--three"><span></span></div>

      <section class="programs">
        <h2>On Demand Diplomate/Certificate<br>Programs:</h2>
        <ul>
          <li>Chiropractic Neurology Diplomate</li>
          <li>Functional Medicine &amp; Nutrition<br>Certificate Program</li>
          <li>Acupuncture Certification Program</li>
          <li>Anti Aging Certificate Program</li>
        </ul>
      </section>

      <aside class="assistant-cta">
        <h3>Certify Your Chiropractic Assistants!</h3>
        <p>On Demand Online course for CA's- makes eligible to take<br>online CALB exam for CA Certification</p>
      </aside>
    </div>
  </div>
</div>
</body>
</html>
```